Commercial construction business needs a great sales brochure!

We are smaller commercial construction company in the Minneapolis, MN market that is looking for a professional sales brochure that can be used to market our services at trade shows or meetings with potential clients. We provide commercial membrane flat roofing, siding and construction services. The final design should communicate trust, growth and safety.

```html
<!DOCTYPE html>
<html lang="en">
<head>
<meta charset="utf-8">
<title>Ridgeline Commercial – Sales Brochure</title>
<link href="https://fonts.googleapis.com/css2?family=Montserrat:wght@500;700;800&family=Open+Sans:wght@400;600;700&display=swap" rel="stylesheet">
<style>
:root{
  --red:#b3131c;
  --red-dark:#7d0d13;
  --ink:#2a2a2c;
  --grey:#e9e9ea;
  --grey-mid:#bfc0c2;
  --white:#ffffff;
  --photo-a:#6f6a63;
  --photo-b:#3d3b3a;
}
*{box-sizing:border-box;margin:0;padding:0}
html,body{width:885px;height:1200px;overflow:hidden;background:#f4f4f4}
body{position:relative;font-family:"Open Sans",Arial,sans-serif;color:var(--ink)}
.spread{position:absolute;left:25px;width:835px;height:565px;display:flex;box-shadow:0 2px 8px rgba(0,0,0,.25);background:var(--white)}
.spread--cover{top:28px}
.spread--inside{top:612px}
.page{position:relative;width:50%;height:100%;overflow:hidden}
.page+.page{border-left:1px solid #d6d6d6}

/* cover */
.cover-art{position:absolute;inset:0}
.brand{position:absolute;top:18px;left:0;right:0;text-align:center;font-family:"Montserrat",sans-serif}
.brand-mark{display:inline-block;width:34px;height:34px;background:var(--red);margin-bottom:6px}
.brand-name{font-weight:800;font-size:15px;color:var(--red);letter-spacing:.5px;line-height:1.1}
.brand-sub{font-weight:800;font-size:15px;color:var(--red);font-size:8px;letter-spacing:1.5px}
.cover-headline{position:absolute;left:0;right:0;top:262px;text-align:center;color:var(--white);font-family:"Montserrat",sans-serif;font-weight:800;font-size:17px;line-height:1.3;text-transform:uppercase;padding:0 40px}
.badge{position:absolute;width:150px;height:150px;border-radius:50%;background:var(--red);color:var(--white);display:flex;flex-direction:column;justify-content:center;align-items:center;text-align:center;border:4px solid rgba(255,255,255,.85)}
.badge--contact{left:-18px;bottom:22px;padding-left:16px}
.badge--contact h3{font-family:"Montserrat",sans-serif;font-size:13px;font-weight:700;letter-spacing:1px}
.badge--contact p{font-size:8px;margin-top:4px}
.socials{display:flex;gap:4px;margin-top:5px}
.socials span{width:10px;height:10px;border-radius:50%;background:var(--white)}
.badge--mission{right:-18px;bottom:22px;padding-right:18px;font-family:"Montserrat",sans-serif;font-weight:700;font-size:7.5px;line-height:1.4}
.badge--mission small{display:block;font-weight:500;font-size:6px;margin-top:6px}

/* inside left */
.why{position:absolute;top:0;left:0;right:0;height:165px;background:var(--grey);padding:18px 24px}
.section-title{font-family:"Montserrat",sans-serif;font-weight:800;font-size:18px;color:var(--red);text-transform:uppercase}
.why p{font-size:6.6px;line-height:1.45;margin-top:6px;color:#444}
.why .question{font-weight:700;font-size:7.5px;color:var(--ink);margin-top:8px}
.projects{position:absolute;top:168px;left:0;right:0;text-align:center}
.projects .section-title{font-size:14px;color:var(--red)}
.project-row{display:flex;gap:8px;justify-content:center;margin-top:8px}
.project-photo{width:124px;height:88px;background:linear-gradient(160deg,#8e9aa5,#4e5359)}
.features{position:absolute;top:300px;left:0;right:0;height:232px;background:var(--grey);display:flex;gap:10px;padding:14px 18px}
.feature{flex:1;background:var(--white);padding:26px 10px 10px;position:relative;text-align:center}
.feature--dark{background:#4a4b4e;color:var(--white)}
.feature-icon{position:absolute;top:-4px;left:50%;transform:translateX(-50%);width:26px;height:26px;border-radius:50%;background:var(--red)}
.feature h4{font-family:"Montserrat",sans-serif;font-size:8px;font-weight:700;margin-top:4px}
.feature p{font-size:6px;line-height:1.5;margin-top:6px;color:inherit;opacity:.8}
.feature .more{display:inline-block;margin-top:8px;background:var(--red);color:var(--white);font-size:6px;padding:3px 8px}
.footer-band{position:absolute;left:0;right:0;bottom:0;height:33px;background:var(--red);color:var(--white);font-size:8px;font-weight:600;text-align:center;line-height:33px}

/* inside right */
.services{position:absolute;top:0;left:0;right:0;height:212px;background:linear-gradient(135deg,#5b5d61,#2f3033)}
.services-inner{position:absolute;inset:0;background:rgba(30,30,32,.55);padding:22px 30px;color:var(--white)}
.services .section-title{color:var(--white);font-size:17px;text-align:center}
.services-intro{font-size:6.5px;line-height:1.5;text-align:center;margin:6px auto 0;width:270px;opacity:.85}
.service-grid{display:grid;grid-template-columns:repeat(3,1fr);row-gap:10px;margin-top:12px}
.service{text-align:center;font-size:7px;font-weight:600}
.service svg{display:block;margin:0 auto 3px}
.partners{position:absolute;top:228px;left:0;right:0;text-align:center}
.partners .section-title{color:var(--ink);font-size:16px}
.partner-grid{display:grid;grid-template-columns:repeat(4,72px);gap:20px 18px;justify-content:center;margin-top:18px}
.partner-badge{height:34px;background:var(--grey-mid);border-radius:3px}
.partner-badge--red{background:#d3a3a6}
.partner-badge--dark{background:#8b8e94}
</style>
</head>
<body>

<section class="spread spread--cover">
  <article class="page page--back">
    <svg class="cover-art" viewBox="0 0 417 565" preserveAspectRatio="none" role="img" aria-label="Aerial photo of a multi-family apartment complex with a red tint">
      <defs><linearGradient id="aerialA" x1="0" y1="0" x2="1" y2="1"><stop offset="0" stop-color="#8a8178"/><stop offset="1" stop-color="#3e3c3b"/></linearGradient></defs>
      <rect width="417" height="565" fill="url(#aerialA)"/>
      <rect width="417" height="565" fill="#7d0d13" opacity=".35"/>
      <polygon points="0,0 417,0 417,215 0,150" fill="#b3131c"/>
      <polygon points="0,0 417,0 417,195 0,135" fill="#ffffff"/>
    </svg>
    <div class="brand"><span class="brand-mark"></span><div class="brand-name">RIDGELINE COMMERCIAL</div><div class="brand-sub">ROOFING &amp; CONSTRUCTION</div></div>
    <h2 class="cover-headline">We are your commercial, multi-family, and residential partners</h2>
    <div class="badge badge--contact">
      <h3>CONTACT US</h3>
      <div class="socials"><span></span><span></span><span></span><span></span></div>
      <p>(555) 014-2290</p>
      <p>ridgelinecommercial.example</p>
    </div>
  </article>
  <article class="page page--front">
    <svg class="cover-art" viewBox="0 0 417 565" preserveAspectRatio="none" role="img" aria-label="Aerial photo of commercial flat roofs with a red tint">
      <defs><linearGradient id="aerialB" x1="1" y1="0" x2="0" y2="1"><stop offset="0" stop-color="#8a8178"/><stop offset="1" stop-color="#3e3c3b"/></linearGradient></defs>
      <rect width="417" height="565" fill="url(#aerialB)"/>
      <rect width="417" height="565" fill="#7d0d13" opacity=".35"/>
      <polygon points="0,0 417,0 417,150 0,215" fill="#b3131c"/>
      <polygon points="0,0 417,0 417,135 0,195" fill="#ffffff"/>
    </svg>
    <div class="brand"><span class="brand-mark"></span><div class="brand-name">RIDGELINE COMMERCIAL</div><div class="brand-sub">ROOFING &amp; CONSTRUCTION</div></div>
    <h2 class="cover-headline">Value driven. Proven results. Celebrating over 10-years of service.</h2>
    <div class="badge badge--mission">We are your commercial, multi-family and residential partners in roofing, siding and construction<small>hello@ridgelinecommercial.example</small></div>
  </article>
</section>

<section class="spread spread--inside">
  <article class="page page--left">
    <div class="why">
      <h2 class="section-title">Why choose us?</h2>
      <p>With over ten years of hands-on experience in roofing, siding and construction, our crew delivers dependable work on every project. We focus on clear communication, safe job sites and lasting quality so property owners can rely on us from the first inspection to the final walkthrough.</p>
      <p class="question">Do you have a property that is in need of an update?</p>
      <p>Whether it is a flat membrane roof, new siding or a full exterior renovation, we build plans around your budget and schedule. Contact our team today for a free estimate and see how we can protect and improve your investment.</p>
    </div>
    <div class="projects">
      <h2 class="section-title">Recent projects</h2>
      <div class="project-row">
        <div class="project-photo" role="img" aria-label="Photo of a finished commercial roof project"></div>
        <div class="project-photo" role="img" aria-label="Photo of a flat membrane roof installation"></div>
        <div class="project-photo" role="img" aria-label="Photo of a multi-family building exterior"></div>
      </div>
    </div>
    <div class="features">
      <div class="feature"><span class="feature-icon"></span><h4>Quality Guarantee</h4><p>We stand behind every job with trusted materials and skilled crews who do it right.</p><span class="more">Read More</span></div>
      <div class="feature feature--dark"><span class="feature-icon"></span><h4>Safety First</h4><p>Trained teams follow strict safety standards on every site we work.</p><span class="more">Read More</span></div>
      <div class="feature"><span class="feature-icon"></span><h4>Over 10 Years Experience</h4><p>A decade of roofing and construction projects across the region.</p><span class="more">Read More</span></div>
    </div>
    <div class="footer-band">www.ridgelinecommercial.example</div>
  </article>

  <article class="page page--right">
    <div class="services" role="img" aria-label="Photo of a roofer working on a commercial roof">
      <div class="services-inner">
        <h2 class="section-title">Our services</h2>
        <p class="services-intro">From membrane flat roofing to full exterior construction, we offer complete services for commercial and residential properties.</p>
        <div class="service-grid">
          <div class="service"><svg width="24" height="24" viewBox="0 0 24 24"><circle cx="12" cy="12" r="12" fill="#b3131c"/><path d="M6 13l6-5 6 5M8 12v5h8v-5" fill="none" stroke="#fff" stroke-width="1.5"/></svg>Roofing</div>
          <div class="service"><svg width="24" height="24" viewBox="0 0 24 24"><circle cx="12" cy="12" r="12" fill="#b3131c"/><path d="M7 8h10M7 11h10M7 14h10M7 17h10" stroke="#fff" stroke-width="1.4"/></svg>Siding</div>
          <div class="service"><svg width="24" height="24" viewBox="0 0 24 24"><circle cx="12" cy="12" r="12" fill="#b3131c"/><rect x="7" y="7" width="10" height="10" fill="none" stroke="#fff" stroke-width="1.4"/><path d="M12 7v10M7 12h10" stroke="#fff" stroke-width="1.2"/></svg>Window Installation</div>
          <div class="service"><svg width="24" height="24" viewBox="0 0 24 24"><circle cx="12" cy="12" r="12" fill="#b3131c"/><path d="M7 17l7-7M12 7h5v3" fill="none" stroke="#fff" stroke-width="1.6"/></svg>Construction Services</div>
          <div class="service"><svg width="24" height="24" viewBox="0 0 24 24"><circle cx="12" cy="12" r="12" fill="#b3131c"/><path d="M8 16l6-6M14 8a2.5 2.5 0 1 0 2 2" fill="none" stroke="#fff" stroke-width="1.6"/></svg>Repair Services</div>
          <div class="service"><svg width="24" height="24" viewBox="0 0 24 24"><circle cx="12" cy="12" r="12" fill="#b3131c"/><path d="M12 6l5 2v4c0 3-2 5-5 6-3-1-5-3-5-6V8z" fill="none" stroke="#fff" stroke-width="1.4"/></svg>Insurance Restoration</div>
        </div>
      </div>
    </div>
    <div class="partners">
      <h2 class="section-title">Trusted partners</h2>
      <div class="partner-grid">
        <div class="partner-badge"></div><div class="partner-badge partner-badge--dark"></div><div class="partner-badge"></div><div class="partner-badge partner-badge--dark"></div>
        <div class="partner-badge partner-badge--red"></div><div class="partner-badge"></div><div class="partner-badge partner-badge--dark"></div><div class="partner-badge partner-badge--red"></div>
        <div class="partner-badge partner-badge--dark"></div><div class="partner-badge"></div><div class="partner-badge partner-badge--red"></div><div class="partner-badge"></div>
      </div>
    </div>
    <div class="footer-band">www.ridgelinecommercial.example</div>
  </article>
</section>

</body>
</html>
```